Talent Management Company Needs Business Cards

Using one of the logos provided (attached) K&K Talent Collective needs a business card designed.
Please visit our website for more information about us-

www.kktalentcollective.net

The face should feature a dramatic presentation of the logo with the back being reserved for our professional information which is:

The information should be:
Darnell T. Fosbury
C.E.O
Email: dtfosbury@kktalentcollective.net
Mobile: 216-555-0193
Website: www.kktalentcollective.net

Marcus L. Fosbury
Director of Public Relations
Email: mlfosbury@kktalentcollective.net
Mobile: 216-555-0147

Rory J. Whitcomb
Director of Client Development
Email: rwhitcomb@kktalentcollective.net

Glenn Strauss
Director of Brand Development
Email: gstrauss@kktalentcollective.net

Would like the logo to have color. I would like to see one side red or black and the other side white but if it looks better in either black or red that would be fine to but would like to see how it comes out.

Please feel free to message me and if you would like just the icon alone I have other image files that I can send as well.

Target Market(s)

Professional Athletes, coaches, entertainers age 18-35 but also must be accepted in the business community

Industry/Entity Type

Business

Requirements
Must have
• 1) Use the logo
2) Double sided
3) Distinctive
Nice to have
• Small simple images for telephone, e-mail, and Url.

```html
<!DOCTYPE html>
<html lang="en">
<head>
<meta charset="utf-8">
<title>K&amp;K Talent Collective — Business Cards</title>
<link href="https://fonts.googleapis.com/css2?family=Open+Sans:wght@400;600&display=swap" rel="stylesheet">
<style>
  :root {
    --stage: #e4e4e4;
    --paper: #ffffff;
    --ink: #2b2b2b;
    --ink-soft: #4a4a4a;
    --red: #e3141b;
    --red-deep: #6e0004;
    --black: #0d0d0d;
    --card-shadow: 0 6px 14px rgba(0,0,0,0.28);
  }
  * { box-sizing: border-box; margin: 0; padding: 0; }
  html, body { width: 1200px; height: 900px; overflow: hidden; }
  body {
    background: radial-gradient(ellipse at center, #f6f6f6 0%, var(--stage) 70%, #d6d6d6 100%);
    font-family: "Open Sans", Arial, sans-serif;
    position: relative;
  }
  .card {
    position: absolute;
    width: 510px;
    height: 312px;
    border-radius: 16px;
    box-shadow: var(--card-shadow);
    overflow: hidden;
  }
  .card--front-top { left: 66px; top: 114px; }
  .card--front-bottom { left: 66px; top: 473px; }
  .card--back-black { left: 619px; top: 114px; background: linear-gradient(180deg, #1a1a1a, var(--black)); }
  .card--back-red { left: 619px; top: 473px; background: radial-gradient(ellipse at 20% 0%, #ff1a1f 0%, var(--red) 25%, #a8050b 65%, var(--red-deep) 100%); }

  /* Information side */
  .info { background: var(--paper); }
  .info__accent {
    position: absolute; right: 0; top: 42px;
    width: 11px; height: 98px; background: var(--red);
  }
  .info__name {
    position: absolute; left: 41px; top: 76px;
    font-size: 15px; font-weight: 600; color: var(--ink);
  }
  .info__title {
    position: absolute; left: 41px; top: 98px;
    font-size: 11.5px; color: var(--ink-soft);
  }
  .info__brand {
    position: absolute; right: 44px; top: 60px;
    display: flex; flex-direction: column; align-items: center; gap: 12px;
  }
  .info__brand-mark { width: 22px; height: 22px; background: var(--red); }
  .info__brand-name {
    font-size: 14px; font-weight: 600; color: var(--black); letter-spacing: 0.3px;
  }
  .info__address {
    position: absolute; right: 316px; top: 238px;
    text-align: right; font-size: 11.5px; line-height: 17px; color: var(--ink);
  }
  .info__divider {
    position: absolute; left: 217px; top: 242px;
    width: 2px; height: 48px; background: var(--red);
  }
  .info__contacts {
    position: absolute; left: 233px; top: 238px;
    list-style: none; font-size: 11.5px; line-height: 17px; color: var(--ink);
  }
  .info__contacts li { display: flex; align-items: center; gap: 7px; }
  .info__contacts svg { width: 12px; height: 12px; fill: var(--ink); flex: none; }

  /* Logo side */
  .face__brand {
    position: absolute; left: 0; right: 0; top: 84px;
    display: flex; flex-direction: column; align-items: center; gap: 26px;
  }
  .face__brand-mark { width: 60px; height: 60px; border-radius: 50%; }
  .card--back-black .face__brand-mark { background: var(--red); }
  .card--back-red .face__brand-mark { background: #ffffff; }
  .face__brand-name {
    font-size: 20px; font-weight: 600; color: #ffffff; letter-spacing: 0.5px;
  }
  .face__url {
    position: absolute; left: 0; right: 0; top: 271px;
    text-align: center; font-size: 14px; color: #ffffff; letter-spacing: 0.2px;
  }
</style>
</head>
<body>

  <svg width="0" height="0" style="position:absolute">
    <defs>
      <symbol id="icon-mail" viewBox="0 0 12 12"><path d="M0 2h12v8H0z M1 3v.4l5 3.2 5-3.2V3z M1 4.6V9h10V4.6L6 7.8z" fill-rule="evenodd"/></symbol>
      <symbol id="icon-phone" viewBox="0 0 12 12"><path d="M3 0h6a1 1 0 0 1 1 1v10a1 1 0 0 1-1 1H3a1 1 0 0 1-1-1V1a1 1 0 0 1 1-1zm0.6 1.3v8h4.8v-8zM5.4 10h1.2v1H5.4z" fill-rule="evenodd"/></symbol>
      <symbol id="icon-home" viewBox="0 0 12 12"><path d="M6 0.5 0 6h1.8v5.5h3V8h2.4v3.5h3V6H12z"/></symbol>
    </defs>
  </svg>

  <section class="card card--front-top info">
    <div class="info__accent"></div>
    <p class="info__name">Marcus L. Fosbury</p>
    <p class="info__title">Director of Public Relations</p>
    <div class="info__brand">
      <span class="info__brand-mark"></span>
      <span class="info__brand-name">K&amp;K TALENT COLLECTIVE</span>
    </div>
    <address class="info__address" style="font-style:normal">
      1180 Harbor Ridge Rd<br>Suite 410<br>Cincinnati, OH 45299
    </address>
    <div class="info__divider"></div>
    <ul class="info__contacts">
      <li><svg><use href="#icon-mail"/></svg>mlfosbury@kktalentcollective.net</li>
      <li><svg><use href="#icon-phone"/></svg>216-555-0147</li>
      <li><svg><use href="#icon-home"/></svg>www.kktalentcollective.net</li>
    </ul>
  </section>

  <section class="card card--back-black face">
    <div class="face__brand">
      <span class="face__brand-mark"></span>
      <span class="face__brand-name">K&amp;K TALENT COLLECTIVE</span>
    </div>
    <p class="face__url">www.kktalentcollective.net</p>
  </section>

  <section class="card card--front-bottom info">
    <div class="info__accent"></div>
    <p class="info__name">Marcus L. Fosbury</p>
    <p class="info__title">Director of Public Relations</p>
    <div class="info__brand">
      <span class="info__brand-mark"></span>
      <span class="info__brand-name">K&amp;K TALENT COLLECTIVE</span>
    </div>
    <address class="info__address" style="font-style:normal">
      1180 Harbor Ridge Rd<br>Suite 410<br>Cincinnati, OH 45299
    </address>
    <div class="info__divider"></div>
    <ul class="info__contacts">
      <li><svg><use href="#icon-mail"/></svg>mlfosbury@kktalentcollective.net</li>
      <li><svg><use href="#icon-phone"/></svg>216-555-0147</li>
      <li><svg><use href="#icon-home"/></svg>www.kktalentcollective.net</li>
    </ul>
  </section>

  <section class="card card--back-red face">
    <div class="face__brand">
      <span class="face__brand-mark"></span>
      <span class="face__brand-name">K&amp;K TALENT COLLECTIVE</span>
    </div>
    <p class="face__url">www.kktalentcollective.net</p>
  </section>

</body>
</html>
```